To design a new professional and elegant website design

To design an elegant and professional business website - e.g. Responsive Pressa theme.

Please refer to the existing site www.verlow-partners.com for information regarding the business service and the content that will be included.

While the designer can suggest colors, the current logo (see attached) should remain.
Although I have indicated Sans Serif as a font, I welcome alternative suggestions.
Updates

To all designers:

I have attached additional .psd files of the logo for your use in the design of the new site (theme). As posted in an earlier response, I wish to keep the logo and the color blue. You are welcome to either work with or change the green.

- Please avoid making the page too busy.

- Avoid stock business pictures such as the people working on a document with the calculator the generic people in suits. Ideally, I would like unique media.

- Do not include contact information on the home page. There are two offices – 1 in Houston and one in UK and I want to make sure that we distinguish between the two.

- Use bullets rather than check boxes .

- Do not use the social links as we do not currently use them - this may change in the future

- The footer should include: sitemap, Terms of Use, Privacy Policy and the 2014 Copyright notice. The other pages should be accessible via a menu

Hope this helps.
Thanks

To all participants,

I have increased the budget by an additional £200.

Regards,

Target Market(s)

As you may glean from the website, the company is a management consultancy serving Meridale 400 companies and private equity firms. Companies include: Tolk, GX, KF, Navine Rosset Companies, Selo Varna...

Sites that may influence the design include:

http://www.hvn.co.uk/consulting/
http://www.qz.com/UK/en/Services/Advisory
http://www.kolt.com/industry-expertise/technology/index.aspx
http://www.obvaleprojects.com/news

Industry/Entity Type

Business Service

Font styles to use
Sans Serif

Colors

Designer to choose colors to be used in the design.

Requirements
Must have
• Existing blue logo - globe with the V & P (see attached). The green is not necessary
Must function of a Pressa responsive platform.
Nice to have
• While the new theme will need to be consistent throughout the site, the home page can vary from the child pages.
Should not have
• Common stock images. If used, the images and icons should be unique.

```html
<!DOCTYPE html>
<html lang="en">
<head>
<meta charset="utf-8">
<title>Verlow Partners</title>
<link href="https://fonts.googleapis.com/css2?family=Open+Sans:ital,wght@0,400;0,600;1,400&family=Rosario:wght@400;500&display=swap" rel="stylesheet">
<style>
:root{
  --blue:#1e78d2;
  --green:#6fae1f;
  --green-dark:#4f8a10;
  --ink:#333;
  --text:#666;
  --muted:#888;
  --line:#dcdcdc;
  --panel:rgba(60,64,70,.82);
  --footer:#5f5f5f;
  --white:#fff;
}
*{margin:0;padding:0;box-sizing:border-box}
html,body{width:1060px;height:1200px;overflow:hidden;background:var(--white)}
body{position:relative;font-family:"Open Sans",Arial,sans-serif;color:var(--text)}
.abs{position:absolute}

/* header */
.brand{left:113px;top:28px;display:flex;align-items:center;gap:10px}
.brand-mark{width:60px;height:60px;border:4px solid var(--blue);border-radius:50%}
.brand-name{font-family:"Rosario",sans-serif;font-size:19px;line-height:20px;color:#555;letter-spacing:.3px}
.nav{top:65px;font-size:13px;color:#333;white-space:nowrap}
.nav.active{color:var(--green)}
.nav .caret{font-size:9px;margin-left:3px}
.nav.faq{font-size:15px;top:63px}

/* hero */
.hero{left:0;top:113px;width:1060px;height:317px;
  background:linear-gradient(180deg,#2f7fe0 0%,#5aa2ec 40%,#a9d1f5 72%,#7fbf3a 86%,#4e9a22 100%)}
.dropdown{left:541px;top:115px;width:141px;background:rgba(70,70,70,.9)}
.dropdown div{height:27px;line-height:27px;padding-left:17px;font-size:12.5px;color:#eee}
.dropdown .current{color:var(--green);border-bottom:1px solid #555}
.tagline{left:592px;height:35px;line-height:35px;padding-left:11px;background:var(--panel);color:var(--white);font-family:"Rosario",sans-serif;font-size:17px;letter-spacing:.2px}
.cta{left:593px;top:317px;width:124px;height:34px;line-height:34px;text-align:center;background:var(--green);border-radius:2px;color:var(--white);font-size:12.5px}

/* testimonials */
.h-section{font-family:"Rosario",sans-serif;font-size:19.5px;color:#555}
.h-welcome{font-size:24px}
.portrait{left:115px;width:64px;height:65px;border:1px solid #ddd;background:linear-gradient(180deg,#e9e9e9,#9a9a9a)}
.quote{font-style:italic;font-size:10.5px;line-height:15px;color:#777}
.author{font-size:10.5px;color:#333}

/* features */
.intro{left:495px;top:512px;width:460px;font-size:12.5px;line-height:18px;color:#777}
.feature-icon{left:490px;width:36px;height:36px}
.feature-title{left:548px;font-size:14.5px;color:#333}
.feature-body{left:548px;width:400px;font-size:12.5px;line-height:17.5px;color:#888}

/* partners */
.divider{left:108px;top:978px;width:843px;height:1px;background:var(--line)}
.sep{top:1016px;width:1px;height:70px;background:#e4e4e4}
.partner{top:1040px;font-family:"Rosario",sans-serif;font-size:20px;color:#9a9a9a;text-align:center}
.arrow{top:1038px;width:26px;height:26px}

/* footer */
.footer{left:0;top:1121px;width:1060px;height:79px;background:var(--footer)}
.footer-links,.copyright{top:1152px;font-size:10.5px;color:#f2f2f2}
.footer-links span{margin:0 6px}
</style>
</head>
<body>

<header>
  <div class="abs brand">
    <div class="brand-mark"></div>
    <div class="brand-name">VERLOW<br>PARTNERS</div>
  </div>
  <div class="abs nav active" style="left:470px">HOME</div>
  <div class="abs nav" style="left:543px">ABOUT VERLOW<span class="caret">v</span></div>
  <div class="abs nav" style="left:666px">VALUES<span class="caret">v</span></div>
  <div class="abs nav" style="left:755px">CLIENTS &amp; SERVICES<span class="caret">v</span></div>
  <div class="abs nav faq" style="left:910px">FAQs</div>
</header>

<section>
  <div class="abs hero" role="img" aria-label="Photo of a businessman in a suit with arms outstretched under a blue sky over a green field, banknotes flying around him"></div>
  <div class="abs dropdown">
    <div class="current">VERLOW TEAM</div>
    <div>CONTACT</div>
  </div>
  <div class="abs tagline" style="top:233px;width:373px">Big, strong and reliable International Company</div>
  <div class="abs tagline" style="top:271px;width:296px">with corresponding office worldwide</div>
  <div class="abs cta">LEARN ABOUT US</div>
</section>

<section>
  <h2 class="abs h-section" style="left:111px;top:468px">What people are saying about us:</h2>

  <div class="abs portrait" style="top:518px" role="img" aria-label="Portrait of an older man"></div>
  <p class="abs quote" style="left:192px;top:523px;width:215px">""Lorem ipsum dolor sit amet, consectetuer adipiscing elit. Aenean commodo ligula eget dolor. Aenean massa. Cum sociis natoque penatibus et magnis.""</p>
  <p class="abs author" style="left:117px;top:590px">– Harlan Prewitt , CEO , Orbis Design</p>

  <p class="abs quote" style="left:117px;top:620px;width:240px">""Nullam dictum felis eu pede mollis pretium. Integer tincidunt. Cras dapibus.""</p>
  <p class="abs author" style="left:117px;top:664px">– Neil Baskow , Brightwell Inc.</p>

  <div class="abs portrait" style="top:695px" role="img" aria-label="Portrait of a woman"></div>
  <p class="abs quote" style="left:192px;top:699px;width:215px">""Lorem ipsum dolor sit amet, consectetuer adipiscing elit. Aenean commodo ligula eget dolor. Aenean massa. Cum sociis natoque penatibus et magnis.""</p>
  <p class="abs author" style="left:116px;top:773px">– Marta Selwyn, Freelancer - Writer</p>

  <div class="abs portrait" style="top:811px" role="img" aria-label="Portrait of a woman"></div>
  <p class="abs quote" style="left:192px;top:815px;width:215px">""Lorem ipsum dolor sit amet, consectetuer adipiscing elit. Aenean commodo ligula eget dolor. Aenean massa. Cum sociis natoque penatibus et magnis.""</p>
  <p class="abs author" style="left:116px;top:889px">– Marta Selwyn, Freelancer - Writer</p>
</section>

<section>
  <h1 class="abs h-section h-welcome" style="left:495px;top:467px">Welcome to Verlow Partners</h1>
  <p class="abs intro">In enim justo, rhoncus ut, imperdiet a, venenatis vitae, justo. Nullam dictum felis eu pede mollis pretium. Integer tincidunt. Cras dapibus. Vivamus elementum semper nisi. Aenean vulputate eleifend tellus.</p>

  <svg class="abs feature-icon" style="top:578px" viewBox="0 0 36 36" fill="none" stroke="#888" stroke-width="1.6">
    <circle cx="18" cy="18" r="16"/><path d="M18 8v10l-7 4M18 18l6-6"/>
    <circle cx="8" cy="22" r="1.2" fill="#888"/><circle cx="28" cy="22" r="1.2" fill="#888"/>
  </svg>
  <h3 class="abs feature-title" style="top:587px;font-weight:400">Lorem ipsum dolor sit amet</h3>
  <p class="abs feature-body" style="top:626px">Lorem ipsum dolor sit amet, consectetuer adipiscing elit. Aenean commodo ligula eget dolor. Aenean massa. Cum sociis natoque penatibus et magnis dis parturient montes, nascetur ridiculus mus. Donec quam felis, ultricies nec.</p>

  <svg class="abs feature-icon" style="top:703px;width:40px" viewBox="0 0 40 36" fill="none" stroke="#888" stroke-width="2">
    <circle cx="11" cy="11" r="6" stroke-dasharray="3 2" stroke-width="4"/><circle cx="11" cy="11" r="2.5"/>
    <circle cx="26" cy="22" r="8" stroke-dasharray="3.5 2.5" stroke-width="5"/><circle cx="26" cy="22" r="3.5"/>
    <circle cx="8" cy="26" r="4" stroke-dasharray="2.5 2" stroke-width="3"/>
  </svg>
  <h3 class="abs feature-title" style="top:713px;font-weight:400">Aenean massa cum sociis natoque penatibus</h3>
  <p class="abs feature-body" style="top:752px">In enim justo, rhoncus ut, imperdiet a, venenatis vitae, justo. Nullam dictum felis eu pede mollis pretium. Integer tincidunt. Cras dapibus. Vivamus elementum semper nisi. Aenean vulputate eleifend tellus.</p>

  <svg class="abs feature-icon" style="top:812px" viewBox="0 0 36 36" fill="none" stroke="#999" stroke-width="1.3">
    <circle cx="18" cy="18" r="15"/><ellipse cx="18" cy="18" rx="7" ry="15"/>
    <path d="M3 18h30M5 11h26M5 25h26M18 3v30"/>
  </svg>
  <h3 class="abs feature-title" style="top:821px;font-weight:400">Aenean massa cum sociis natoque penatibus</h3>
  <p class="abs feature-body" style="top:860px">In enim justo, rhoncus ut, imperdiet a, venenatis vitae, justo. Nullam dictum felis eu pede mollis pretium. Integer tincidunt. Cras dapibus. Vivamus elementum semper nisi. Aenean vulputate eleifend tellus.</p>
</section>

<section>
  <div class="abs divider"></div>
  <svg class="abs arrow" style="left:217px" viewBox="0 0 26 26" fill="none" stroke="#bbb" stroke-width="1.5"><path d="M24 13H2M12 3L2 13l10 10"/></svg>
  <div class="abs partner" style="left:255px;width:80px">Halvex</div>
  <div class="abs sep" style="left:344px"></div>
  <div class="abs partner" style="left:365px;width:90px">Quarno</div>
  <div class="abs sep" style="left:473px"></div>
  <div class="abs partner" style="left:490px;width:85px">Mintra</div>
  <div class="abs sep" style="left:588px"></div>
  <div class="abs partner" style="left:605px;width:90px">Dovely</div>
  <div class="abs sep" style="left:708px"></div>
  <div class="abs partner" style="left:725px;width:80px">Pressa</div>
  <svg class="abs arrow" style="left:808px" viewBox="0 0 26 26" fill="none" stroke="#bbb" stroke-width="1.5"><path d="M2 13h22M14 3l10 10-10 10"/></svg>
</section>

<footer>
  <div class="abs footer"></div>
  <div class="abs footer-links" style="left:113px">Sitemap<span>|</span>Terms of Use<span>|</span>Privacy Policy</div>
  <div class="abs copyright" style="left:680px">Copyright © 2014 Verlow Partners. All Rights Reserved.</div>
</footer>

</body>
</html>
```